Crestline Slate & Tile Needs a Business Card

Attached you will find your logo, my photo and design guidelines for a new business card. The final design will need two separate files to create an embossed card. The cards will be printed by www.plinkprint.com (Instructions below)
Format is the Zib SQUARE card
Crestline Slate And Tile is a brick and mortar, retail stone and tile shop.
One the front:
Crestline Slate And Tile
Gerald Finchcombe
Owner
48207 Vesper Hollow Blvd
Suite R & T
Charlotte, NC 28953
Cell: 704-555-0183
Web: www.CrestlineSlateAndTile.com
(Make each word of the domain a different or alternating color)
On the back;
Something that shows beautiful colorful tile
Follow the design guide closely please. For more information see this page that describes creating the spot gloss file: https://www.plinkprint.com/us/business-cards/design-guidelines-spot-gloss
The logo is what we would like to have raised spot glossed.
Format is the Zib SQUARE card. See attahced guidlines.

```html
<!DOCTYPE html>
<html lang="en">
<head>
<meta charset="utf-8">
<title>Crestline Slate &amp; Tile – Business Card</title>
<link href="https://fonts.googleapis.com/css2?family=Cormorant+Garamond:wght@500;600&family=Montserrat:wght@400;500&display=swap" rel="stylesheet">
<style>
  :root {
    --slate: #2c3946;
    --slate-deep: #222d38;
    --ink: #22303c;
    --rust: #b4471f;
    --gold: #d49a2a;
    --sage: #8a8f78;
    --paper: #ffffff;
    --stage: #d9dadc;
  }
  * { margin: 0; padding: 0; box-sizing: border-box; }
  html, body { width: 1200px; height: 900px; overflow: hidden; }
  body {
    background: var(--stage);
    display: flex; align-items: center; justify-content: center; gap: 60px;
  }
  .card { width: 470px; height: 470px; position: relative; overflow: hidden; }

  /* Back side */
  .card-back { background: var(--slate); }
  .tile-field {
    position: absolute; inset: 0;
    background: radial-gradient(circle at 50% 45%, #34424f 0%, var(--slate) 55%, var(--slate-deep) 100%);
  }
  .back-brand {
    position: absolute; inset: 0;
    display: flex; flex-direction: column; align-items: center; justify-content: center; gap: 30px;
  }
  .brand-square { width: 86px; height: 86px; background: var(--gold); }
  .back-brand .brand-name {
    font-family: "Cormorant Garamond", serif; font-weight: 600;
    font-size: 25px; letter-spacing: 3px; text-transform: uppercase; color: var(--paper);
  }

  /* Front side */
  .card-front { background: var(--paper); }
  .front-brand {
    position: absolute; left: 32px; top: 46px;
    display: flex; align-items: center; gap: 28px;
  }
  .front-brand .brand-square { width: 96px; height: 96px; }
  .front-brand .brand-name {
    font-family: "Cormorant Garamond", serif; font-weight: 600;
    font-size: 40px; line-height: 1.05; letter-spacing: 2px; text-transform: uppercase; color: var(--ink);
  }
  .person-name {
    position: absolute; left: 33px; top: 198px;
    font-family: "Cormorant Garamond", serif; font-weight: 600; font-size: 28px; color: var(--ink);
  }
  .person-role {
    position: absolute; left: 33px; top: 233px;
    font-family: "Montserrat", sans-serif; font-size: 14px; letter-spacing: 0.5px; color: var(--rust);
  }
  .divider {
    position: absolute; left: 33px; top: 263px; width: 315px; height: 0;
    border-top: 2px dashed var(--ink);
  }
  .portrait {
    position: absolute; left: 346px; top: 210px; width: 92px; height: 92px;
    background: linear-gradient(160deg, #5d4a3e, #2b2f36);
    border: 2px solid var(--gold);
  }
  .address {
    position: absolute; left: 33px; top: 280px;
    font-family: "Montserrat", sans-serif; font-size: 14.5px; line-height: 25.5px; color: var(--ink);
    font-style: normal;
  }
  .contact-list {
    position: absolute; left: 33px; top: 364px; list-style: none;
    font-family: "Montserrat", sans-serif; font-size: 14.5px; line-height: 25px; color: var(--ink);
  }
  .contact-list li { display: flex; align-items: center; gap: 6px; }
  .contact-list svg { width: 15px; height: 15px; flex: none; }
  .phone { letter-spacing: 2px; }
  .word-a { color: var(--rust); }
  .word-b { color: var(--gold); }
  .word-c { color: var(--sage); }
</style>
</head>
<body>

  <section class="card card-back" aria-label="Card back">
    <div class="tile-field" role="img" aria-label="Embossed repeating slate tile pattern"></div>
    <div class="back-brand">
      <div class="brand-square"></div>
      <div class="brand-name">Crestline Slate &amp; Tile</div>
    </div>
  </section>

  <section class="card card-front" aria-label="Card front">
    <div class="front-brand">
      <div class="brand-square"></div>
      <div class="brand-name">Crestline<br>Slate &amp; Tile</div>
    </div>

    <h1 class="person-name">Gerald Finchcombe</h1>
    <p class="person-role">Owner</p>
    <div class="divider"></div>
    <div class="portrait" role="img" aria-label="Portrait photo of the owner"></div>

    <address class="address">
      48207 Vesper Hollow Blvd<br>
      Suite R &amp; T<br>
      Charlotte, NC 28953
    </address>

    <ul class="contact-list">
      <li>
        <svg viewBox="0 0 24 24" aria-hidden="true"><path fill="#b4471f" d="M6.6 10.8a15 15 0 0 0 6.6 6.6l2.2-2.2c.3-.3.7-.4 1-.2 1.1.4 2.3.6 3.6.6.6 0 1 .4 1 1V20c0 .6-.4 1-1 1A17 17 0 0 1 3 4c0-.6.4-1 1-1h3.5c.6 0 1 .4 1 1 0 1.3.2 2.5.6 3.6.1.3 0 .7-.2 1z"/></svg>
        <span class="phone">704-555-0183</span>
      </li>
      <li>
        <svg viewBox="0 0 24 24" aria-hidden="true"><rect x="2" y="5" width="20" height="14" fill="#b4471f"/><path d="M2 5l10 8 10-8" fill="none" stroke="#fff" stroke-width="1.8"/></svg>
        <span>info@<span class="word-a">Crestline</span><span class="word-b">Slate</span><span class="word-c">And</span><span class="word-b">Tile</span>.com</span>
      </li>
      <li>
        <svg viewBox="0 0 24 24" aria-hidden="true"><g fill="none" stroke="#b4471f" stroke-width="2"><circle cx="12" cy="12" r="9"/><ellipse cx="12" cy="12" rx="4" ry="9"/><path d="M3 12h18M5 7h14M5 17h14"/></g></svg>
        <span>www.<span class="word-a">Crestline</span><span class="word-b">Slate</span><span class="word-c">And</span><span class="word-b">Tile</span>.com</span>
      </li>
    </ul>
  </section>

</body>
</html>
```